Business card and stationary for NMV Counseling
NMV Counseling - Bramblewood Support Circle, LLC
Business card and stationary for NMV Counseling - Health
Creative Brief
Bright & Fun-filled
Daniel H. Ostrander
MS, MBA, RMHCI
NMV Counseling Bramblewood Support Circle, LLC 4870 W Hazelmere Avenue Orlando, FL 32806
nmvcounseling@mailvista.example
www.nmvcounseling.example
KPT58371
Tie colors into website: www.nmvcounseling.example I'd like to see options for a one side and two sided card.
Text for back of card to include: Next Appointment For: Date: Time: If you are unable to keep appointment, please provide at least 24 hours notice to avoid a fee. === Individual Couples Men's Issues Business Professionals Career Counseling

```html
<!DOCTYPE html>
<html lang="en">
<head>
<meta charset="utf-8">
<title>NMV Counseling — Stationery</title>
<link rel="stylesheet" href="https://fonts.googleapis.com/css2?family=Open+Sans:wght@400;600;700&display=swap">
<style>
  :root {
    --navy: #2e2c7d;
    --navy-deep: #23216a;
    --sky: #8fb3e0;
    --sky-soft: #c9dbf1;
    --paper: #ffffff;
    --ink: #4a4a5a;
    --ink-soft: #8a8a98;
    --backdrop: #e6e7ea;
  }
  * { margin: 0; padding: 0; box-sizing: border-box; }
  html, body { width: 1200px; height: 799px; overflow: hidden; }
  body {
    background: var(--backdrop);
    font-family: "Open Sans", Arial, sans-serif;
    color: var(--ink);
    position: relative;
  }
  .sheet {
    position: absolute;
    background: var(--paper);
    box-shadow: 0 6px 18px rgba(0,0,0,.12);
    overflow: hidden;
  }
  .brand { display: flex; align-items: center; gap: 8px; }
  .brand-dot { border-radius: 50%; background: var(--sky); flex: none; }
  .brand-name {
    font-weight: 700; color: var(--navy);
    text-transform: uppercase; letter-spacing: .06em; white-space: nowrap;
  }
  .band { position: absolute; display: block; }

  /* Letterhead */
  .letterhead { left: 60px; top: 40px; width: 540px; height: 719px; }
  .letterhead .brand { position: absolute; left: 48px; top: 44px; }
  .letterhead .brand-dot { width: 26px; height: 26px; }
  .letterhead .brand-name { font-size: 20px; }
  .letterhead .letter-body {
    position: absolute; left: 48px; top: 130px; width: 420px;
    font-size: 11.5px; line-height: 1.75;
  }
  .letter-body p { margin-bottom: 14px; }
  .letterhead .band { left: 0; bottom: 0; width: 540px; height: 120px; }
  .letterhead .footer-contact {
    position: absolute; left: 48px; bottom: 22px;
    font-size: 9.5px; line-height: 1.6; color: var(--paper);
  }

  /* Envelope */
  .envelope { left: 640px; top: 40px; width: 500px; height: 250px; }
  .envelope .brand { position: absolute; left: 26px; top: 24px; }
  .envelope .brand-dot { width: 16px; height: 16px; }
  .envelope .brand-name { font-size: 13px; }
  .envelope .return-address {
    position: absolute; left: 26px; top: 52px;
    font-size: 8.5px; line-height: 1.55; color: var(--ink-soft);
  }
  .envelope .recipient {
    position: absolute; left: 210px; top: 118px;
    font-size: 10px; line-height: 1.7; color: var(--ink);
  }
  .envelope .band { right: 0; bottom: 0; width: 500px; height: 90px; }

  /* Business cards */
  .card { width: 340px; height: 194px; }
  .card-front { left: 640px; top: 330px; }
  .card-back { left: 800px; top: 560px; }
  .card-front .brand { position: absolute; left: 22px; top: 24px; }
  .card-front .brand-dot { width: 14px; height: 14px; }
  .card-front .brand-name { font-size: 12px; }
  .card-front .person { position: absolute; left: 22px; top: 66px; }
  .person-name { font-size: 13px; font-weight: 700; color: var(--navy); }
  .person-title { font-size: 9px; color: var(--ink-soft); letter-spacing: .05em; }
  .card-front .band { left: 0; bottom: 0; width: 340px; height: 70px; }
  .card-front .card-contact {
    position: absolute; left: 22px; bottom: 10px;
    font-size: 7.5px; line-height: 1.5; color: var(--paper);
  }
  .card-back { background: var(--navy); }
  .card-back .appointment {
    position: absolute; left: 22px; top: 18px; width: 190px;
    font-size: 8.5px; line-height: 1.6; color: var(--paper);
  }
  .appointment-title { font-weight: 700; font-size: 10px; margin-bottom: 4px; }
  .appointment-line { border-bottom: 1px solid var(--sky); padding-top: 6px; }
  .appointment-note { margin-top: 10px; font-size: 7.5px; color: var(--sky-soft); }
  .card-back .services {
    position: absolute; right: 20px; top: 22px; list-style: none;
    font-size: 8.5px; line-height: 1.9; color: var(--paper); text-align: right;
  }
  .card-back .license {
    position: absolute; right: 20px; bottom: 14px; font-size: 7px; color: var(--sky-soft);
  }
</style>
</head>
<body>

<section class="sheet letterhead">
  <div class="brand"><span class="brand-dot"></span><span class="brand-name">NMV Counseling</span></div>
  <div class="letter-body">
    <p>Dear Client,</p>
    <p>Thank you for choosing our practice. We offer a calm, private space where individuals and couples can talk openly, set goals and build lasting habits for a steadier, brighter life.</p>
    <p>Sessions are held in person or online, with flexible evening hours. Please arrive a few minutes early so we can begin on time and make the most of each visit.</p>
    <p>We look forward to working with you.</p>
    <p>Warm regards,<br><strong>Daniel H. Ostrander</strong><br>MS, MBA, RMHCI</p>
  </div>
  <svg class="band" viewBox="0 0 540 120" preserveAspectRatio="none" aria-hidden="true">
    <path d="M0 50 C180 10 360 90 540 20 L540 120 L0 120 Z" fill="var(--sky)"/>
    <path d="M0 62 C180 24 360 104 540 36 L540 120 L0 120 Z" fill="var(--navy)"/>
  </svg>
  <div class="footer-contact">
    Bramblewood Support Circle, LLC · 4870 W Hazelmere Avenue Orlando, FL 32806<br>
    nmvcounseling@mailvista.example · www.nmvcounseling.example
  </div>
</section>

<section class="sheet envelope">
  <div class="brand"><span class="brand-dot"></span><span class="brand-name">NMV Counseling</span></div>
  <div class="return-address">
    Bramblewood Support Circle, LLC<br>
    4870 W Hazelmere Avenue<br>
    Orlando, FL 32806
  </div>
  <div class="recipient">Recipient Name<br>Street Address<br>City, State ZIP</div>
  <svg class="band" viewBox="0 0 500 90" preserveAspectRatio="none" aria-hidden="true">
    <path d="M180 90 C300 70 400 40 500 0 L500 90 Z" fill="var(--sky)"/>
    <path d="M230 90 C330 74 420 50 500 18 L500 90 Z" fill="var(--navy)"/>
  </svg>
</section>

<section class="sheet card card-front">
  <div class="brand"><span class="brand-dot"></span><span class="brand-name">NMV Counseling</span></div>
  <div class="person">
    <div class="person-name">Daniel H. Ostrander</div>
    <div class="person-title">MS, MBA, RMHCI</div>
  </div>
  <svg class="band" viewBox="0 0 340 70" preserveAspectRatio="none" aria-hidden="true">
    <path d="M0 14 C120 0 230 26 340 4 L340 70 L0 70 Z" fill="var(--sky)"/>
    <path d="M0 22 C120 8 230 34 340 12 L340 70 L0 70 Z" fill="var(--navy)"/>
  </svg>
  <div class="card-contact">
    4870 W Hazelmere Avenue Orlando, FL 32806<br>
    nmvcounseling@mailvista.example · www.nmvcounseling.example
  </div>
</section>

<section class="sheet card card-back">
  <div class="appointment">
    <div class="appointment-title">Next Appointment For:</div>
    <div class="appointment-line">Date:</div>
    <div class="appointment-line">Time:</div>
    <p class="appointment-note">If you are unable to keep appointment, please provide at least 24 hours notice to avoid a fee.</p>
  </div>
  <ul class="services">
    <li>Individual</li>
    <li>Couples</li>
    <li>Men's Issues</li>
    <li>Business Professionals</li>
    <li>Career Counseling</li>
  </ul>
  <div class="license">KPT58371</div>
</section>

</body>
</html>
```